Visitenkarten/Briefpaier/Kassenkassenbelege für Juwelier
Zielgruppe
Mittelständischer Juwelier mit zwei Filialen. Klassischer Schmuck, Uhren und Modeschmuck
Aufgabenstellung
Es müssen für zwei Geschäfte Visitenkarten, Briefpapier (A4) und Kassenkassenbelege (A6) erstellt werden. Logo und fenwiro im Anhang. Ein Farbkonzept besteht noch nicht. Die Idee geht in Richtung Bordeaux-Rot.
Generell:
(1) Sieht erstmal nach viel Beschreibung aus, bitte nicht entmutigen lassen, sind zu 90% nur austauschbare Inhalts-/Kontaktdaten.
(2) Für meine Zwecke reicht es vollkommen aus, wenn bei den Vorschlägen zur Arbeitsersparnis erstmal nur mit einer Adresse gearbeitet wird. Wenn ich dann den zutreffenden Designvorschlag gefunden habe, können wir die zweite Adresse in dem ersten Format umsetzen. Ich denke das spart Zeit und Nerven.
(3) Bitte Angaben wie "Tel.:" oder "USt.- ID:" nicht wörtlich nehmen, es soll dabei klar sein worum es geht; wenn "Telefon" ausgeschrieben besser aussieht, bitte in der optisch ansprechenderen Form verwenden.
(4) Bei Fragen, bitte fragen!
(5) Viel Spass bei dem Projekt - Ich freu' mich auf die Vorschläge!
Visitenkarten(1):
Juwelier Brandauer GmbH
www.juwelier-brandauer-example.de
Visitenkarten(2):
Visitenkarten(generell):
(1) Die einzelnen Daten können durch Hervorhebungen wie Adresse, Kontakt, Online/Internet unterteilt bzw. hervorgehoben werden.
(2) Die Visitenkarten sollen farbig gedruckt werden; geplant ist weiß als Hintergrund ist aber nicht zwingend bei einer guten anderen Idee
Briefpapier:
(1)Absender im Adressfeld für DIN-lang Briefumschläge mit Fenster:
(2)Informationen im Footer/Seitenbereich:
Juwelier Brandauer Gmb..

```html
<!DOCTYPE html>
<html lang="de">
<head>
<meta charset="utf-8">
<title>Juwelier Brandauer – Visitenkarte</title>
<link href="https://fonts.googleapis.com/css2?family=Open+Sans:wght@400;600;700&display=swap" rel="stylesheet">
<style>
  :root {
    --stage: #e9eaec;
    --card-white: #f7f7f8;
    --lavender: #a4abc0;
    --lavender-text: #8d94b0;
    --stone: #7c7c7c;
    --ink: #6d6d6d;
    --white: #ffffff;
  }
  * { box-sizing: border-box; margin: 0; padding: 0; }
  html, body { width: 1200px; height: 800px; overflow: hidden; }
  body {
    background: var(--stage);
    font-family: "Open Sans", Arial, sans-serif;
    position: relative;
  }
  .card {
    position: absolute;
    top: 238px;
    width: 500px;
    height: 324px;
    overflow: hidden;
    box-shadow: 0 2px 8px rgba(0,0,0,0.12);
  }
  /* Front */
  .card--front { left: 70px; background: var(--lavender); }
  .front__mark {
    position: absolute;
    left: 215px; top: 42px;
    width: 70px; height: 70px;
    background: var(--white);
  }
  .front__name {
    position: absolute;
    left: 0; right: 0; top: 128px;
    text-align: center;
    color: var(--stone);
    font-weight: 600;
    font-size: 32px;
    letter-spacing: 0.03em;
    text-transform: uppercase;
    white-space: nowrap;
  }
  .front__tagline {
    position: absolute;
    left: 0; right: 0; top: 178px;
    text-align: center;
    color: var(--white);
    font-weight: 700;
    font-size: 15px;
    letter-spacing: 0.42em;
    text-transform: uppercase;
    white-space: nowrap;
  }
  .front__since {
    position: absolute;
    left: 0; right: 0; top: 202px;
    text-align: center;
    color: var(--white);
    font-weight: 600;
    font-size: 8px;
    letter-spacing: 0.2em;
    text-transform: uppercase;
  }
  .front__rule {
    position: absolute;
    left: 110px; right: 110px; top: 220px;
    height: 1px;
    background: var(--stone);
  }
  .front__accent {
    position: absolute;
    left: 310px; bottom: 0;
    width: 48px; height: 42px;
    background: var(--stone);
  }
  /* Back */
  .card--back { left: 630px; background: var(--card-white); }
  .back__mark {
    position: absolute;
    left: 40px; top: 0;
    width: 56px; height: 44px;
    background: var(--stone);
  }
  .back__mark-inner {
    position: absolute;
    left: 56px; top: 0;
    width: 44px; height: 44px;
    background: var(--lavender);
  }
  .back__info {
    position: absolute;
    left: 40px; top: 96px;
    font-size: 14px;
    line-height: 1.65;
    color: var(--lavender-text);
    white-space: nowrap;
  }
  .back__company { color: var(--ink); font-weight: 700; text-transform: uppercase; letter-spacing: 0.02em; }
  .back__label { color: var(--ink); font-weight: 700; }
  .back__web { color: var(--ink); }
  .back__web strong { font-weight: 700; }
  .back__accent {
    position: absolute;
    right: 60px; bottom: 0;
    width: 52px; height: 42px;
    background: var(--lavender);
  }
</style>
</head>
<body>
  <section class="card card--front" aria-label="Visitenkarte Vorderseite">
    <div class="front__mark"></div>
    <div class="front__name">Juwelier Brandauer</div>
    <div class="front__tagline">Uhren &amp; Schmuck</div>
    <div class="front__since">Seit 1980</div>
    <div class="front__rule"></div>
    <div class="front__accent"></div>
  </section>

  <section class="card card--back" aria-label="Visitenkarte Rückseite">
    <div class="back__mark"></div>
    <div class="back__mark-inner"></div>
    <div class="back__info">
      <p class="back__company">Juwelier Brandauer GmbH</p>
      <p>Goldschmiedeweg 14 | 37081 Feldhausen a.d. Leine</p>
      <p><span class="back__label">TEL</span> 0551-738204 &nbsp;<span class="back__label">FAX</span> 0551-738205</p>
      <p><span class="back__label">info@</span>juwelier-brandauer-example.de</p>
      <p class="back__web"><strong>www.</strong>juwelier-brandauer-example.de</p>
    </div>
    <div class="back__accent"></div>
  </section>
</body>
</html>
```